Food delivery wordpress design

need food delivery wordpress design for my site, here's the requirements
1. site must be pixel perfect , clean and professional
2. logo provided and must be match with the color scheme
3. pages : home , about us , faq , vendor registration

*** this is a information site no order can be made from the site, the site will show how things work , how to register as vendor , how to use the app , you may use any stock photo from pictorvane and send me the code, i will purchase it

you may use any of the logo to play with it

***** It must look scale and not looks like template where I can purchase elsewhere

the designer told me he can't work as he got his personal problem, please check his message

those who prefer to purchase online

Sans Serif

• refer to zelvo.com/my
• everything user and vendor like to know

```html
<!DOCTYPE html>
<html lang="en">
<head>
<meta charset="utf-8">
<title>Saji Saji – Food Delivery</title>
<link rel="stylesheet" href="https://fonts.googleapis.com/css2?family=Rubik:wght@500;700;800&family=Roboto:wght@400;500;700&display=swap">
<style>
:root{
  --orange:#e6982f;
  --orange-deep:#e08a1e;
  --orange-soft:#f6b23c;
  --ink:#1d1d1d;
  --text:#555;
  --muted:#e3e3e3;
  --card:#f5f5f5;
  --line:#e6e6e6;
  --footer:#3d3d3d;
  --white:#fff;
}
*{box-sizing:border-box;margin:0;padding:0}
html,body{width:1200px;height:4402px;overflow:hidden}
body{font-family:'Roboto',sans-serif;color:var(--text);background:var(--white);position:relative}
.abs{position:absolute}
h1,h2,.step-num{font-family:'Rubik',sans-serif}

/* header */
.site-header{position:absolute;left:0;top:0;width:1200px;height:79px;background:var(--white);border-bottom:1px solid var(--line)}
.brand{position:absolute;left:120px;top:22px;display:flex;align-items:center;gap:10px}
.brand-dot{width:30px;height:30px;border-radius:50%;background:var(--orange)}
.brand-name{font-family:'Rubik',sans-serif;font-weight:700;font-size:26px;color:#333}
.main-nav{position:absolute;left:521px;top:32px;display:flex;gap:22px;font-size:13px;font-weight:700;color:#222}
.main-nav .active{color:var(--orange)}
.search-btn{position:absolute;left:1039px;top:21px;width:41px;height:41px;border-radius:50%;background:var(--orange)}

/* hero */
.hero{position:absolute;left:0;top:79px;width:1200px;height:557px;background:var(--orange)}
.hero-pattern{position:absolute;inset:0;background:radial-gradient(circle at 30% 40%,rgba(255,255,255,.06),transparent 60%)}
.hero-title{position:absolute;left:109px;top:158px;font-size:51px;line-height:60px;font-weight:800;color:var(--white)}
.hero-mascot{position:absolute;left:675px;top:75px;width:440px;height:410px;border-radius:50%;background:radial-gradient(circle,#f8b13a 0 45%,rgba(60,60,60,.25) 46% 55%,transparent 56%)}

.section-title{position:absolute;left:0;width:1200px;text-align:center;font-size:39px;font-weight:700;color:var(--ink)}

/* app steps */
.step-text{position:absolute;width:420px}
.step-num{font-size:52px;font-weight:800;color:var(--muted);line-height:1}
.step-icon{width:40px;height:34px;margin:10px 0 14px;border-radius:6px;background:linear-gradient(135deg,#f9c46a,var(--orange))}
.step-text p{font-size:13.5px;line-height:26px;color:#666}
.step-link{display:inline-flex;align-items:center;gap:8px;margin-top:10px;font-size:13px;font-weight:700;color:var(--orange);text-decoration:underline}
.step-photo{position:absolute;width:439px;height:282px;border:4px solid var(--white);box-shadow:0 0 8px rgba(0,0,0,.25)}

/* how things work */
.work-bg{position:absolute;left:0;top:1870px;width:1200px;height:1120px;background:linear-gradient(180deg,#fff,#f7f7f7 30%,#fafafa 70%,#fff)}
.work-card{position:absolute;top:2200px;width:249px;height:201px;background:var(--card);border-left:3px solid var(--orange);border-bottom:3px solid var(--orange);padding:50px 20px 0 20px}
.work-card::before{content:"";position:absolute;left:-3px;top:0;width:70px;height:3px;background:var(--orange)}
.work-card::after{content:"";position:absolute;right:-3px;bottom:-3px;width:3px;height:140px;background:var(--orange)}
.work-card .dot{position:absolute;right:-9px;top:56px;width:16px;height:16px;border-radius:50%;background:var(--orange)}
.work-pin{position:absolute;top:2111px;width:99px;height:99px;border-radius:50%;background:var(--orange);border:7px solid var(--orange-soft)}
.work-pin::before{content:"";position:absolute;left:14px;top:14px;width:57px;height:57px;border-radius:50%;background:var(--white)}
.work-pin::after{content:"";position:absolute;left:38px;top:88px;border:11px solid transparent;border-top:14px solid var(--orange)}
.work-step{font-size:14px;font-weight:500;color:var(--orange)}
.work-head{font-size:15px;font-weight:700;color:var(--orange);margin:8px 0 10px}
.work-card p{font-size:13.5px;line-height:23px;color:#666}

/* vendor */
.vendor-card{position:absolute;top:2628px;width:236px;height:252px;background:var(--white);border:1px solid #eee;box-shadow:0 0 8px rgba(0,0,0,.1);text-align:center;padding-top:24px}
.vendor-icon{width:82px;height:82px;border-radius:50%;margin:0 auto 28px;background:radial-gradient(circle,#f4a940 0 30%,#fde0b5 32%)}
.vendor-card h3{font-size:15px;font-weight:700;color:var(--orange);margin-bottom:8px}
.vendor-card p{font-size:13.5px;line-height:21px;color:#666;padding:0 14px}

/* about */
.about{position:absolute;left:0;top:2987px;width:1200px;height:469px;background:linear-gradient(90deg,#f2a33a 0,#f2a84a 30%,#b79f7e 55%,#5f6e72 85%,#3d4d55 100%)}
.about-photo{position:absolute;left:400px;top:0;width:800px;height:469px;background:linear-gradient(90deg,transparent,rgba(120,100,70,.4) 40%,rgba(60,80,90,.5))}
.about h2{position:absolute;left:111px;top:68px;font-size:37px;font-weight:700;color:var(--white)}
.about p{position:absolute;left:111px;top:127px;width:425px;font-size:13.5px;line-height:28.5px;color:#fff7e8}
.btn-learn{position:absolute;left:111px;top:349px;width:156px;height:48px;border-radius:24px;background:#d9822a;color:var(--white);font-size:13px;font-weight:700;display:flex;align-items:center;justify-content:center;gap:8px}

/* faq */
.faq{position:absolute;left:0;top:3456px;width:1200px;height:651px;background:linear-gradient(180deg,#fbfbfb,#ededed 50%,#f3efea)}
.faq-item{position:absolute;left:212px;width:776px;background:var(--white);padding:0 35px}
.faq-q{display:flex;justify-content:space-between;align-items:center;height:53px;font-size:13px;font-weight:500;color:#222}
.faq-q span:last-child{font-size:20px;font-weight:700}
.faq-a{font-size:13px;line-height:26px;color:#777;margin-top:-4px}

/* footer */
.site-footer{position:absolute;left:0;top:4107px;width:1200px;height:295px;background:var(--footer);color:var(--white);text-align:center}
.social{position:absolute;left:523px;top:55px;display:flex;gap:19px}
.social span{width:38px;height:38px;border-radius:50%;border:2px solid var(--white)}
.contact-row{position:absolute;left:0;top:128px;width:1200px;display:flex;justify-content:center;gap:28px;font-size:14px;align-items:center}
.contact-row .sep{width:1px;height:18px;background:#aaa}
.contact-row span{display:inline-flex;align-items:center;gap:12px}
.footer-nav{position:absolute;left:0;top:183px;width:1200px;display:flex;justify-content:center;gap:22px;font-size:13px;font-weight:700}
.copyright{position:absolute;left:0;top:231px;width:1200px;font-size:13.5px}
</style>
</head>
<body>

<header class="site-header">
  <div class="brand"><span class="brand-dot"></span><span class="brand-name">sajisaji</span></div>
  <nav class="main-nav">
    <span class="active">HOME</span><span>ABOUT US</span><span>FAQ</span><span>VENDOR REGISTRATION</span><span>CONTACT US</span>
  </nav>
  <span class="search-btn">
    <svg width="41" height="41" viewBox="0 0 41 41"><circle cx="19" cy="19" r="6" fill="none" stroke="#fff" stroke-width="2.5"/><line x1="23.5" y1="23.5" x2="28" y2="28" stroke="#fff" stroke-width="2.5" stroke-linecap="round"/></svg>
  </span>
</header>

<section class="hero">
  <div class="hero-pattern" role="img" aria-label="Faint line pattern of food doodles"></div>
  <h1 class="hero-title">Despite These<br>Uncertain Times,<br>We're Still Here<br>To Serve You</h1>
  <div class="hero-mascot" role="img" aria-label="Illustrated running chef-hat mascot"></div>
</section>

<h2 class="section-title" style="top:733px">How To Use The App</h2>

<div class="step-text" style="left:118px;top:895px">
  <div class="step-num">01</div><div class="step-icon"></div>
  <p>Lorem ipsum dolor sit amet, consectetur adipiscing elit, sed do eiusmod tempor incididunt ut labore et dolore magna aliqua. Ut enim ad minim veniam, quis nostrud</p>
  <span class="step-link">DOWNLOAD THE APP <svg width="12" height="12"><circle cx="6" cy="6" r="6" fill="#e6982f"/><path d="M4 3l3 3-3 3" stroke="#fff" stroke-width="1.6" fill="none"/></svg></span>
</div>
<div class="step-photo" style="left:649px;top:865px;background:linear-gradient(120deg,#8c8f7d,#c9c4b4 45%,#a9713f 80%)" role="img" aria-label="Photo of a courier handing a salad box to a customer"></div>

<div class="step-photo" style="left:111px;top:1219px;background:linear-gradient(120deg,#d9d6d0,#8c7f70 50%,#c49a6c)" role="img" aria-label="Photo of a man unpacking a paper delivery bag on a sofa"></div>
<div class="step-text" style="left:648px;top:1246px">
  <div class="step-num">02</div><div class="step-icon"></div>
  <p>Lorem ipsum dolor sit amet, consectetur adipiscing elit, sed do eiusmod tempor incididunt ut labore et dolore magna aliqua. Ut enim ad minim veniam, quis nostrud</p>
  <span class="step-link">DOWNLOAD THE APP <svg width="12" height="12"><circle cx="6" cy="6" r="6" fill="#e6982f"/><path d="M4 3l3 3-3 3" stroke="#fff" stroke-width="1.6" fill="none"/></svg></span>
</div>

<div class="step-text" style="left:118px;top:1598px">
  <div class="step-num">03</div><div class="step-icon"></div>
  <p>Lorem ipsum dolor sit amet, consectetur adipiscing elit, sed do eiusmod tempor incididunt ut labore et dolore magna aliqua. Ut enim ad minim veniam, quis nostrud</p>
  <span class="step-link">DOWNLOAD THE APP <svg width="12" height="12"><circle cx="6" cy="6" r="6" fill="#e6982f"/><path d="M4 3l3 3-3 3" stroke="#fff" stroke-width="1.6" fill="none"/></svg></span>
</div>
<div class="step-photo" style="left:649px;top:1569px;background:linear-gradient(120deg,#4a3a2c,#8a6a4c 45%,#b89478 75%,#3d2f25)" role="img" aria-label="Photo of friends sharing a meal at a restaurant table"></div>

<div class="work-bg" role="img" aria-label="Faint sketched vegetable pattern background"></div>
<h2 class="section-title" style="top:2002px">How Things Work</h2>

<div class="work-pin" style="left:131px"></div>
<div class="work-card" style="left:55px"><span class="dot"></span><div class="work-step">STEP - 01</div><div class="work-head">LOREM IPSUM DOLOR SIT</div><p>Sed ut perspiciatis unde omnis iste natus error sit voluptatem accusantium doloremque</p></div>
<div class="work-pin" style="left:408px"></div>
<div class="work-card" style="left:333px"><span class="dot"></span><div class="work-step">STEP - 02</div><div class="work-head">LOREM IPSUM DOLOR SIT</div><p>Sed ut perspiciatis unde omnis iste natus error sit voluptatem accusantium doloremque</p></div>
<div class="work-pin" style="left:685px"></div>
<div class="work-card" style="left:610px"><span class="dot"></span><div class="work-step">STEP - 03</div><div class="work-head">LOREM IPSUM DOLOR SIT</div><p>Sed ut perspiciatis unde omnis iste natus error sit voluptatem accusantium doloremque</p></div>
<div class="work-pin" style="left:962px"></div>
<div class="work-card" style="left:887px"><span class="dot"></span><div class="work-step">STEP - 04</div><div class="work-head">LOREM IPSUM DOLOR SIT</div><p>Sed ut perspiciatis unde omnis iste natus error sit voluptatem accusantium doloremque</p></div>

<h2 class="section-title" style="top:2522px">How To Register As a Vendor</h2>
<div class="vendor-card" style="left:106px"><div class="vendor-icon" role="img" aria-label="Chef icon"></div><h3>LOREM IPSUM DOLOR SIT</h3><p>Sed ut perspiciatis unde omnis iste natus error sit voaccusantium doloremque laudantium</p></div>
<div class="vendor-card" style="left:357px"><div class="vendor-icon" role="img" aria-label="Food truck icon"></div><h3>LOREM IPSUM DOLOR SIT</h3><p>Sed ut perspiciatis unde omnis iste natus error sit voaccusantium doloremque laudantium</p></div>
<div class="vendor-card" style="left:607px"><div class="vendor-icon" role="img" aria-label="Delivery scooter icon"></div><h3>LOREM IPSUM DOLOR SIT</h3><p>Sed ut perspiciatis unde omnis iste natus error sit voaccusantium doloremque laudantium</p></div>
<div class="vendor-card" style="left:858px"><div class="vendor-icon" role="img" aria-label="Rated restaurant icon"></div><h3>LOREM IPSUM DOLOR SIT</h3><p>Sed ut perspiciatis unde omnis iste natus error sit voaccusantium doloremque laudantium</p></div>

<section class="about">
  <div class="about-photo" role="img" aria-label="Photo of paper takeaway bag and coffee cups on a car seat"></div>
  <h2>About Us</h2>
  <p>Sed ut perspiciatis unde omnis iste natus error sit voluptatem accusantium doloremque laudantium, totam rem aperiam, eaque ipsa quae ab illo inventore veritatis et quasi architecto beatae vitae dicta sunt explicabo. Nemo enim ipsam voluptatem quia voluptas sit aspernatur aut odit aut fugit, sed quia consequuntur magni dolores eos qui ratione voluptatem sequi nesciunt. Neque porro quisquam est, qui dolorem ipsum</p>
  <span class="btn-learn">LEARN MORE <svg width="13" height="13"><circle cx="6.5" cy="6.5" r="6.5" fill="#fff"/><path d="M5 3.5l3 3-3 3" stroke="#d9822a" stroke-width="1.6" fill="none"/></svg></span>
</section>

<section class="faq" role="img" aria-label="Faded photo of a dining table in the background">
</section>
<h2 class="section-title" style="top:3541px">Frequently Asked Questions</h2>
<div class="faq-item" style="top:3640px"><div class="faq-q"><span>LOREM IPSUM DOLOR SIT AMET, CONSECTETUR ADIPISCING ?</span><span>+</span></div></div>
<div class="faq-item" style="top:3715px"><div class="faq-q"><span>LOREM IPSUM DOLOR SIT AMET, CONSECTETUR ADIPISCING LOREM IPSUM DOLOR SIT ?</span><span>+</span></div></div>
<div class="faq-item" style="top:3790px"><div class="faq-q"><span>SED UT PERSPICIATIS UNDE OMNIS ISTE NATUS ERROR SIT VOLUPTATEM ?</span><span>+</span></div></div>
<div class="faq-item" style="top:3864px;height:123px"><div class="faq-q"><span>UT ENIM AD MINIMA VENIAM, QUIS NOSTRUM EXERCITATIONEM ULLAM CORPORIS ?</span><span>-</span></div>
  <p class="faq-a">At vero eos et accusamus et iusto odio dignissimos ducimus qui blanditiis praesentium voluptatum deleniti atque corrupti quos dolores et quas molestias excepturi sint occaecati cupiditat</p></div>

<footer class="site-footer">
  <div class="social" aria-label="Social links"><span></span><span></span><span></span></div>
  <div class="contact-row">
    <span><svg width="14" height="18" viewBox="0 0 14 18"><path d="M7 0a7 7 0 0 0-7 7c0 5 7 11 7 11s7-6 7-11a7 7 0 0 0-7-7z" fill="#fff"/><circle cx="7" cy="7" r="2.5" fill="#3d3d3d"/></svg>Harbor Point, MO 63199 USA</span>
    <i class="sep"></i>
    <span><svg width="16" height="16" viewBox="0 0 16 16"><path d="M3 1l3 3-2 2c1 2 3 4 5 5l2-2 3 3-2 3C7 15 1 9 1 3z" fill="#fff"/></svg>1 800 555 0199</span>
    <i class="sep"></i>
    <span><svg width="18" height="14" viewBox="0 0 18 14"><rect x="1" y="1" width="16" height="12" fill="none" stroke="#fff" stroke-width="1.5"/><path d="M1 1l8 7 8-7" fill="none" stroke="#fff" stroke-width="1.5"/></svg>info@sajisaji.com</span>
  </div>
  <nav class="footer-nav"><span>HOME</span><span>ABOUT US</span><span>FAQ</span><span>VENDOR REGISTRATION</span><span>CONTACT US</span></nav>
  <div class="copyright">© 2021 Saji Saji. All Rights Reserved</div>
</footer>

</body>
</html>
```